Mosquito Residential & Commercial Treatments

The uploaded logo must be integrated as the main theme of the card. I would like it to be modern and eye catching. Maybe some backround images or light silver metallic background.
Space enough at the base for contact info to be put in- phone numbers,emails,names,website.
Space on the back for short blog and lines for hand writing..calling card.
Commercial- golf courses, schools, outdoor function properties, pre event treatments.
Residential- retirement villages, townhome complexes and general houses
Management

```html
<!DOCTYPE html>
<html lang="en">
<head>
<meta charset="UTF-8">
<title>Harbourline Pest Care – Business Card</title>
<link href="https://fonts.googleapis.com/css2?family=Cinzel:wght@400;600&family=Lato:wght@400&display=swap" rel="stylesheet">
<style>
  :root {
    --backdrop: #3a3a3a;
    --silver-light: #f2f2f2;
    --silver-mid: #d4d4d4;
    --silver-dark: #b5b5b5;
    --ink: #1b1b1b;
    --band: #000000;
    --accent-red: #e3202b;
    --accent-red-dark: #9a141b;
    --white: #ffffff;
    --soft-white: #e6e6e6;
    --muted: #5a5a5a;
  }
  * { box-sizing: border-box; margin: 0; padding: 0; }
  html, body {
    width: 1105px;
    height: 1200px;
    overflow: hidden;
    background: var(--backdrop);
  }
  .sheet { position: relative; width: 1105px; height: 1200px; }
  .card {
    position: absolute;
    left: 196px;
    width: 720px;
    height: 411px;
    overflow: hidden;
  }
  .card--front {
    top: 146px;
    background: linear-gradient(160deg, var(--silver-dark) 0%, var(--silver-light) 45%, var(--silver-mid) 100%);
  }
  .card--back {
    top: 602px;
    background: radial-gradient(ellipse at 50% 50%, var(--white) 0%, var(--silver-light) 35%, var(--silver-dark) 100%);
  }

  /* Front */
  .brand {
    position: absolute;
    left: 28px;
    top: 34px;
    font-family: "Cinzel", serif;
    color: var(--ink);
  }
  .brand__name { font-size: 38px; font-weight: 600; line-height: 1; }
  .brand__tagline { font-size: 15px; line-height: 1.2; margin-top: 4px; }

  .contact-band {
    position: absolute;
    left: 0;
    top: 150px;
    width: 560px;
    height: 261px;
    background: var(--band);
  }
  .contact-band--right {
    left: 560px;
    top: 320px;
    width: 160px;
    height: 91px;
  }
  .accent-stripe {
    position: absolute;
    left: 0;
    top: 147px;
    width: 540px;
    height: 40px;
    background: var(--accent-red);
  }
  .decor-area {
    position: absolute;
    left: 420px;
    top: 150px;
    width: 300px;
    height: 261px;
    background: linear-gradient(135deg, var(--accent-red) 0%, var(--accent-red-dark) 100%);
  }

  .person {
    position: absolute;
    left: 28px;
    top: 222px;
    font-family: "Cinzel", serif;
    color: var(--white);
  }
  .person__name { font-size: 26px; font-weight: 600; line-height: 1.2; }
  .person__role { font-size: 19px; color: var(--soft-white); line-height: 1.3; }

  .contact-list {
    position: absolute;
    left: 28px;
    top: 302px;
    list-style: none;
    font-family: "Cinzel", serif;
    font-size: 17px;
    color: var(--white);
  }
  .contact-list li { display: flex; align-items: center; height: 30px; }
  .contact-list svg { width: 15px; height: 15px; margin-right: 16px; fill: var(--white); }

  /* Back */
  .back-brand {
    position: absolute;
    left: 0;
    top: 180px;
    width: 100%;
    display: flex;
    justify-content: center;
    align-items: center;
    gap: 16px;
    font-family: "Cinzel", serif;
    color: var(--ink);
  }
  .back-brand__mark { width: 18px; height: 18px; background: var(--accent-red); }
  .back-brand__name { font-size: 36px; font-weight: 600; line-height: 1; }
  .back-brand__tagline { font-size: 14px; line-height: 1.2; margin-top: 4px; }
  .back-web {
    position: absolute;
    left: 0;
    top: 344px;
    width: 100%;
    text-align: center;
    font-family: "Lato", sans-serif;
    font-size: 17px;
    letter-spacing: 6px;
    color: var(--muted);
  }
</style>
</head>
<body>
<main class="sheet">

  <section class="card card--front">
    <div class="brand">
      <div class="brand__name">Harbourline Pest Care</div>
      <div class="brand__tagline">Residential &amp; Commercial Treatments</div>
    </div>

    <div class="contact-band"></div>
    <div class="contact-band contact-band--right"></div>
    <div class="accent-stripe"></div>
    <div class="decor-area" role="img" aria-label="Large red insect illustration in flight"></div>

    <div class="person">
      <div class="person__name">Daniel Hart</div>
      <div class="person__role">CEO/Founder</div>
    </div>

    <ul class="contact-list">
      <li>
        <svg viewBox="0 0 24 24" aria-hidden="true"><path d="M6.6 10.8a15.1 15.1 0 0 0 6.6 6.6l2.2-2.2a1 1 0 0 1 1-.25 11.4 11.4 0 0 0 3.6.57 1 1 0 0 1 1 1V20a1 1 0 0 1-1 1A17 17 0 0 1 3 4a1 1 0 0 1 1-1h3.5a1 1 0 0 1 1 1c0 1.25.2 2.45.57 3.57a1 1 0 0 1-.25 1z"/></svg>
        555 014 2270
      </li>
      <li>
        <svg viewBox="0 0 24 24" aria-hidden="true"><path d="M2 5h20v14H2z M4 7v.5l8 5 8-5V7l-8 5z" fill-rule="evenodd"/></svg>
        HELLO@HARBOURLINEPEST.COM
      </li>
      <li>
        <svg viewBox="0 0 24 24" aria-hidden="true"><circle cx="12" cy="12" r="10"/><path d="M12 2v20M2 12h20M5 6c4 2 10 2 14 0M5 18c4-2 10-2 14 0" stroke="#000" stroke-width="1.4" fill="none"/></svg>
        WWW.HARBOURLINEPEST.COM
      </li>
    </ul>
  </section>

  <section class="card card--back">
    <div class="back-brand">
      <div>
        <div class="back-brand__name">Harbourline Pest Care</div>
        <div class="back-brand__tagline">Residential &amp; Commercial Treatments</div>
      </div>
      <div class="back-brand__mark"></div>
    </div>
    <div class="back-web">www.harbourlinepest.com</div>
  </section>

</main>
</body>
</html>
```